Tarrow Vitamins Sign

I need to make a sign that looks like a vintage metal sign like you would find in an old pharmacy. I'm attaching a few examples of the look and feel. The text is attached in the word file

```html
<!DOCTYPE html>
<html lang="en">
<head>
<meta charset="utf-8">
<title>Tarrow Vitamins Sign</title>
<link rel="stylesheet" href="https://fonts.googleapis.com/css2?family=Rye&family=Smokum&display=swap">
<style>
  :root {
    --paper: #fdf6e8;
    --gold: #f2b950;
    --gold-deep: #d99a2e;
    --panel: #16141f;
  }
  html, body {
    margin: 0;
    padding: 0;
    width: 1200px;
    height: 822px;
    overflow: hidden;
    background: var(--paper);
  }
  .sign {
    display: block;
    width: 1200px;
    height: 822px;
  }
  .sign__frame { fill: var(--gold); }
  .sign__panel { fill: var(--panel); }
  .sign__rule { stroke: var(--gold); stroke-width: 3; }
  .sign__tagline,
  .sign__subline {
    font-family: "Rye", serif;
    fill: var(--gold);
    text-anchor: middle;
  }
  .sign__tagline { font-size: 46px; }
  .sign__subline { font-size: 44px; }
  .sign__title {
    font-family: "Smokum", serif;
    fill: var(--gold);
    font-size: 300px;
    text-anchor: middle;
  }
</style>
</head>
<body>
<svg class="sign" viewBox="0 0 1200 822" xmlns="http://www.w3.org/2000/svg">
  <defs>
    <radialGradient id="ornament-glow" cx="50%" cy="50%" r="50%">
      <stop offset="0%" stop-color="#f2b950" stop-opacity="0.55"/>
      <stop offset="100%" stop-color="#f2b950" stop-opacity="0.05"/>
    </radialGradient>
  </defs>

  <rect class="sign__frame" x="20" y="18" width="1160" height="786"/>
  <rect class="sign__panel" x="38" y="34" width="1124" height="752"/>

  <rect class="sign__ornament" x="355" y="66" width="495" height="98" rx="40"
        fill="url(#ornament-glow)" role="img" aria-label="Gold scrollwork flourish crowning the sign"/>

  <line class="sign__rule" x1="112" y1="170" x2="1095" y2="170"/>

  <text class="sign__tagline" x="604" y="236" textLength="480" lengthAdjust="spacingAndGlyphs">Since 70,000 BCE</text>

  <text class="sign__title" x="604" y="520" textLength="1020" lengthAdjust="spacingAndGlyphs">Tarrow Vitamins</text>

  <text class="sign__subline" x="604" y="608" textLength="560" lengthAdjust="spacingAndGlyphs">history of humankind</text>

  <line class="sign__rule" x1="112" y1="640" x2="1095" y2="640"/>

  <rect class="sign__ornament" x="355" y="646" width="495" height="98" rx="40"
        fill="url(#ornament-glow)" role="img" aria-label="Gold scrollwork flourish beneath the sign text"/>
</svg>
</body>
</html>
```